Flyer-Design für Abschleppunternehmen
Zielgruppe
Wir sind ein Abschleppunternehmen und sind bestrebt neue Kunden zu gewinnen. Vor allem im Bereich 'Falschparker' suchen wir Firmen/Unternehmen mit Privatparkplätzen, die von fremden Personen zu geparkt werden. Hierzu ist stark darauf hinzuweisen, dass diese Leistung für den Autraggeber völlig kostenlos und ohne Aufwand anzufordern ist.
Aufgabenstellung
Vorschlag DIN Fyler 21x9,8cm . Wir sind ein 24/7 Betrieb. Rufnr. 073845190. Es ist darauf hinzweisen, dass wir ein unternehmen aus der direkten umgebung sind.

```html
<!DOCTYPE html>
<html lang="de">
<head>
<meta charset="utf-8">
<title>Falschparker Flyer</title>
<link href="https://fonts.googleapis.com/css2?family=Roboto:wght@400;500;700&display=swap" rel="stylesheet">
<style>
  :root {
    --yellow: #fdd000;
    --red: #d40000;
    --black: #000000;
    --white: #ffffff;
    --page: #ffffff;
  }
  * { box-sizing: border-box; margin: 0; padding: 0; }
  html, body {
    width: 1200px; height: 1098px; overflow: hidden;
    background: var(--page);
    font-family: "Roboto", Arial, sans-serif;
  }
  .canvas { position: relative; width: 1200px; height: 1098px; }
  .flyer {
    position: absolute; width: 1034px; height: 482px;
    background: var(--yellow);
    box-shadow: 0 2px 12px rgba(0,0,0,0.18);
    overflow: hidden;
  }
  .flyer--front { left: 48px; top: 53px; }
  .flyer--back { left: 130px; top: 572px; }

  .photo {
    position: absolute; left: 0; top: 0; width: 1034px; height: 333px;
    background: linear-gradient(100deg, #6d6a66 0%, #8e8a82 30%, #c9a92a 55%, #e0c21c 70%, #4a5266 100%);
  }
  .headline-box {
    position: absolute; left: 56px; top: 165px; width: 667px; height: 109px;
    background: var(--red); color: var(--white);
    font-weight: 700; font-size: 54px; line-height: 109px;
    padding-left: 42px; white-space: nowrap;
  }
  .service-badge {
    position: absolute; left: 730px; top: 165px; width: 101px; height: 109px;
    background: var(--red);
  }
  .tagline {
    position: absolute; left: 56px; height: 62px;
    background: var(--black); color: var(--white);
    font-weight: 500; font-size: 36px; line-height: 62px;
    padding-left: 42px; white-space: nowrap;
  }
  .tagline--one { top: 294px; width: 550px; }
  .tagline--two { top: 361px; width: 404px; }

  .brand {
    position: absolute; display: flex; align-items: center; gap: 8px;
    color: var(--red); font-weight: 700; white-space: nowrap;
  }
  .brand__mark { background: var(--red); }
  .flyer--front .brand { left: 858px; top: 402px; font-size: 30px; }
  .flyer--front .brand__mark { width: 18px; height: 18px; }
  .flyer--back .brand { left: 748px; top: 300px; font-size: 46px; }
  .flyer--back .brand__mark { width: 26px; height: 26px; }

  .back-heading {
    position: absolute; left: 73px; top: 83px;
    font-weight: 700; font-size: 38.5px; line-height: 46px; color: var(--black);
  }
  .back-copy {
    position: absolute; left: 73px; top: 218px;
    font-weight: 400; font-size: 23px; line-height: 29px; color: var(--black);
  }
  .phone-button {
    position: absolute; left: 73px; top: 322px; width: 432px; height: 61px;
    background: var(--red); color: var(--white);
    font-weight: 700; font-size: 32px; line-height: 61px;
    padding-left: 38px; white-space: nowrap;
  }
</style>
</head>
<body>
<main class="canvas">
  <section class="flyer flyer--front">
    <div class="photo" role="img" aria-label="Foto: gelbes Pannenhilfe-Fahrzeug in einer Tiefgarage neben geparkten Autos"></div>
    <h1 class="headline-box">Falschparker gesichtet?</h1>
    <div class="service-badge">
      <svg width="101" height="109" viewBox="0 0 101 109" aria-label="24/7 Service">
        <path d="M84 40 A40 40 0 1 1 70 20" fill="none" stroke="#fff" stroke-width="4"/>
        <path d="M70 12 L90 18 L84 38" fill="none" stroke="#fff" stroke-width="4"/>
        <text x="50" y="56" text-anchor="middle" fill="#fff" font-family="Roboto, Arial, sans-serif" font-weight="700" font-size="20">24/7</text>
        <text x="50" y="71" text-anchor="middle" fill="#fff" font-family="Roboto, Arial, sans-serif" font-weight="700" font-size="11">SERVICE</text>
      </svg>
    </div>
    <p class="tagline tagline--one">Wir sind Ihr Ansprechpartner</p>
    <p class="tagline tagline--two">aus der Umgebung.</p>
    <div class="brand"><span class="brand__mark"></span>Krunzel</div>
  </section>

  <section class="flyer flyer--back">
    <h2 class="back-heading">Haben Sie einen Falschparker gesehen<br>oder sind selbst betroffen?</h2>
    <p class="back-copy">Nehmen Sie mit uns Kontakt auf und wir übernehmen<br>alles Weitere. Für Sie entstehen dabei keinerlei kosten!</p>
    <p class="phone-button">Rufnummer: 073845190</p>
    <div class="brand"><span class="brand__mark"></span>Krunzel</div>
  </section>
</main>
</body>
</html>
```